Verdant Medispa Business Card

need a business card for our medispa, attached please see the logo.
our website is https://verdantmedispa-example.com

Sorina Belcourt, MD
Internal Medicine

555-204-7193

Sorina@verdantmedispa-example.com

Www.Verdantmedispa-example.com

738 E Harlow Blvd N, Ste 512, Katy, TX 77981

Target Market(s)

MedSpa, Cosmetics, Esthetics

Industry/Entity Type

MedicalSpa

Contact Information for Business Card

Please see the attached business card which i pulled from the internet. I like the idea back as a logo and front with info.

Font styles to use
Decorative

Requirements
Must have
• Color should be matching with Logo and Website theme, Also I like to have QR code for the website

```html
<!DOCTYPE html>
<html lang="en">
<head>
<meta charset="utf-8">
<title>Verdant Medispa Business Card</title>
<link rel="stylesheet" href="https://fonts.googleapis.com/css2?family=Cinzel:wght@400&family=Poppins:wght@300;400&display=swap">
<style>
  :root {
    --backdrop: #9a9a9a;
    --card-dark: #1e1e1e;
    --card-gold: #926f1e;
    --gold: #d6a92e;
    --cream: #f4eee2;
    --white: #ffffff;
    --address: #8f6d1f;
  }
  * { margin: 0; padding: 0; box-sizing: border-box; }
  html, body {
    width: 1200px; height: 1200px; overflow: hidden;
    background: var(--backdrop);
    font-family: "Poppins", sans-serif;
  }
  .card {
    position: absolute; left: 147px; width: 906px;
  }
  .card-front {
    top: 67px; height: 518px; background: var(--card-dark);
  }
  .card-back {
    top: 615px; height: 517px; background: var(--card-gold);
  }
  .brand-name {
    position: absolute; left: 0; right: 0; text-align: center;
    font-family: "Poppins", sans-serif; font-weight: 300;
    letter-spacing: 3px;
    display: flex; justify-content: center; align-items: center; gap: 18px;
  }
  .brand-dot {
    width: 18px; height: 18px; border-radius: 50%;
  }
  .card-front .brand-name { top: 250px; font-size: 62px; color: var(--gold); }
  .card-front .brand-dot { background: var(--gold); }
  .card-back .brand-name { top: 150px; font-size: 58px; color: var(--cream); }
  .card-back .brand-dot { background: var(--cream); }
  .front-url {
    position: absolute; top: 446px; left: 0; right: 0; text-align: center;
    color: var(--gold); font-size: 19px; letter-spacing: 10px;
  }
  .person {
    position: absolute; right: 509px; top: 284px; text-align: right;
    color: var(--cream);
  }
  .person-name {
    font-family: "Cinzel", serif; font-size: 29px; line-height: 38px; white-space: nowrap;
  }
  .person-role {
    font-size: 20px; font-weight: 300; margin-top: 16px;
  }
  .divider {
    position: absolute; left: 429px; top: 283px; width: 2px; height: 90px;
    background: var(--cream);
  }
  .contact-list {
    position: absolute; left: 457px; top: 284px; list-style: none;
    color: var(--cream); font-size: 20px; font-weight: 300;
  }
  .contact-list li {
    display: flex; align-items: center; gap: 10px; height: 29px; white-space: nowrap;
  }
  .contact-icon { width: 20px; height: 20px; flex: none; }
  .address-band {
    position: absolute; left: 0; right: 0; bottom: 0; height: 67px;
    background: var(--white); color: var(--address);
    display: flex; align-items: center; justify-content: center;
    font-size: 20px; letter-spacing: 2.5px;
  }
</style>
</head>
<body>
  <section class="card card-front">
    <div class="brand-name"><span class="brand-dot"></span>Verdant Medispa</div>
    <p class="front-url">www.verdantmedispa-example.com</p>
  </section>

  <section class="card card-back">
    <div class="brand-name"><span class="brand-dot"></span>Verdant Medispa</div>

    <div class="person">
      <p class="person-name">SORINA BELCOURT, MD</p>
      <p class="person-role">Internal Medicine</p>
    </div>
    <div class="divider"></div>

    <ul class="contact-list">
      <li>
        <svg class="contact-icon" viewBox="0 0 20 20" fill="none" stroke="#f4eee2" stroke-width="1.3">
          <circle cx="10" cy="10" r="8.5"/>
          <path d="M8 6.2c1 .2 1.2 1.6.6 2.2.5 1.1 1.1 1.8 2.2 2.3.6-.6 2-.4 2.2.6-.6 1.3-2 1.3-3.2.6-1.4-.9-2.3-2-2.9-3.4C6.5 7.5 6.9 6.5 8 6.2z"/>
        </svg>
        555-204-7193
      </li>
      <li>
        <svg class="contact-icon" viewBox="0 0 20 20" fill="none" stroke="#f4eee2" stroke-width="1.3">
          <circle cx="10" cy="10" r="8.5"/>
          <circle cx="10" cy="10" r="2.2"/>
          <path d="M12.2 8v3c0 1 1.6 1.2 1.8-.4.3-2.6-1.5-4.6-4-4.6a4 4 0 1 0 2 7.4"/>
        </svg>
        Sorina@verdantmedispa-example.com
      </li>
      <li>
        <svg class="contact-icon" viewBox="0 0 20 20" fill="none" stroke="#f4eee2" stroke-width="1.3">
          <circle cx="10" cy="10" r="8.5"/>
          <ellipse cx="10" cy="10" rx="3.8" ry="8.5"/>
          <path d="M1.5 10h17M3 5.5h14M3 14.5h14"/>
        </svg>
        Www.Verdantmedispa-example.com
      </li>
    </ul>

    <div class="address-band">738 E Harlow Blvd N, Ste 512, Katy, TX 77981</div>
  </section>
</body>
</html>
```